Kelvo Auto - help to get me noticed

We not long ago tasked Pixel Harbour to design a logo for my business. I'm happy with the result so would like to have a business card designed as a follow up.

It's an Automotive service and repair business that offers the following -
- Servicing
- General repairs
- Brakes
- Detailing
- Integrity

Kelvo Automotive
Dallin Mereth
0471 926 317

Target Market(s)

Everyday people with the ability to reach out to corporate customers also.

Industry/Entity Type

Automotive

Contact Information for Business Card

Black card, logo, name and phone number on front. Other details on back of card.

```html
<!DOCTYPE html>
<html lang="en">
<head>
<meta charset="utf-8">
<title>Kelvo Automotive — Business Card</title>
<link rel="stylesheet" href="https://fonts.googleapis.com/css2?family=Saira:wght@600;700&display=swap">
<style>
  :root {
    --page: #2a2a2b;
    --card: #131416;
    --card-band: #1c1e21;
    --green: #7cc534;
    --green-dark: #3f9a2a;
    --white: #f4f4f4;
    --rule: #8a8c90;
  }
  * { box-sizing: border-box; margin: 0; padding: 0; }
  html, body {
    width: 1200px; height: 900px; overflow: hidden;
    background: var(--page);
    font-family: "Saira", "Arial Narrow", sans-serif;
    color: var(--white);
  }
  .canvas {
    position: relative; width: 1200px; height: 900px;
    display: flex; flex-direction: column; align-items: center; justify-content: center; gap: 40px;
  }
  .card {
    position: relative; width: 640px; height: 366px;
    background: var(--card);
    box-shadow: 0 14px 30px rgba(0,0,0,.45);
    overflow: hidden;
  }
  .card__band {
    position: absolute; left: 0; right: 0; top: 22px; height: 220px;
    background: linear-gradient(180deg, var(--card-band), var(--card));
  }
  .card__stripe {
    position: absolute; left: 0; right: 0; bottom: 16px; height: 8px;
    display: flex;
  }
  .card__stripe span { display: block; height: 100%; }
  .stripe__green { width: 64px; background: var(--green); }
  .stripe__white { flex: 1; background: var(--white); }

  .brand {
    font-weight: 700; color: var(--green);
    text-transform: uppercase; letter-spacing: 2px; line-height: 1;
    white-space: nowrap;
  }

  /* back */
  .card--back .brand {
    position: absolute; left: 0; right: 0; top: 70px;
    text-align: center; font-size: 40px;
  }
  .card--back .divider {
    position: absolute; left: 130px; right: 70px; top: 140px;
    height: 1px; background: var(--rule);
  }
  .services {
    position: absolute; left: 258px; top: 168px; list-style: none;
  }
  .services li {
    display: flex; align-items: center; gap: 12px;
    font-size: 21px; font-weight: 600; letter-spacing: 1.5px;
    text-transform: uppercase; line-height: 28px;
  }
  .services li::before {
    content: ""; width: 14px; height: 11px;
    background: linear-gradient(180deg, var(--green), var(--green-dark));
  }

  /* front */
  .card--front .brand {
    position: absolute; left: 56px; top: 62px; font-size: 40px;
  }
  .holder {
    position: absolute; left: 64px; top: 206px;
  }
  .holder__name {
    display: inline-block; white-space: nowrap;
    font-size: 27px; font-weight: 700; letter-spacing: 2px; line-height: 34px;
    text-transform: uppercase; padding: 0 18px 10px 0;
    border-bottom: 1px solid var(--rule);
  }
  .holder__phone {
    display: flex; align-items: center; gap: 12px; white-space: nowrap;
    margin-top: 10px; margin-left: -14px;
    font-size: 26px; font-weight: 700; letter-spacing: 1px; line-height: 32px;
  }
  .holder__phone svg { width: 26px; height: 26px; flex: none; }
</style>
</head>
<body>
<main class="canvas">

  <section class="card card--back" aria-label="Back of business card">
    <div class="card__band"></div>
    <div class="brand">Kelvo Automotive</div>
    <div class="divider"></div>
    <ul class="services">
      <li>Servicing</li>
      <li>General Repairs</li>
      <li>Brakes</li>
      <li>Detailing</li>
      <li>Integrity</li>
    </ul>
    <div class="card__stripe"><span class="stripe__green"></span><span class="stripe__white"></span><span class="stripe__green"></span></div>
  </section>

  <section class="card card--front" aria-label="Front of business card">
    <div class="brand">Kelvo Automotive</div>
    <div class="holder">
      <p class="holder__name">Dallin Mereth</p>
      <p class="holder__phone">
        <svg viewBox="0 0 26 26" aria-hidden="true">
          <circle cx="13" cy="13" r="11" fill="none" stroke="var(--green)" stroke-width="2"/>
          <path d="M9 7.5c.6-.5 1.4-.4 1.8.2l1 1.6c.3.5.2 1.100-.2 1.5l-.8.7c.5 1.3 1.6 2.5 2.9 3.1l.7-.8c.4-.4 1-.5 1.5-.2l1.6 1c.6.4.7 1.2.2 1.8l-.8.9c-.6.6-1.5.8-2.300.5-3-1.1-5.3-3.5-6.4-6.5-.3-.8-.1-1.700.5-2.300z" fill="var(--green)"/>
        </svg>
        0471 926 317
      </p>
    </div>
    <div class="card__stripe"><span class="stripe__green"></span><span class="stripe__white"></span><span class="stripe__green"></span></div>
  </section>

</main>
</body>
</html>
```